Design a (20.4 x 10.14) Banner that says - Keep Hope Rising From Harvest Crown TV Family

We want a design (20.4 x 10.14) with the words 'Keep Hope Rising' as the main text and 'From Harvest Crown TV Family' underneath. For 'Harvest Crown TV', we'd like you to use the logo which can be found in the image attached.

The image attached is just an example but please let your creative juices flow!

Target Market(s)

Christian

Industry/Entity Type

Christian

Requirements
Must have
• Must have the words 'Keep Hope Rising' and 'From Harvest Crown TV Family'.

```html
<!DOCTYPE html>
<html lang="en">
<head>
<meta charset="utf-8">
<title>Keep Hope Rising – Harvest Crown TV banners</title>
<link rel="stylesheet" href="https://fonts.googleapis.com/css2?family=Allura&family=Archivo+Black&display=swap">
<style>
  :root {
    --stage: #979797;
    --white: #ffffff;
    --navy: #1f2a6b;
    --violet-deep: #2a1680;
    --violet-mid: #4b2a9a;
    --violet-glow: #5a36d8;
    --teal-deep: #0d4a68;
    --teal-mid: #1a7391;
    --teal-glow: #2aa3c4;
    --bloom-pink: #d7848f;
    --bloom-purple: #9a4fc4;
    --word-pink: #ff5fd0;
    --word-light: #f3e6ff;
    --word-blue: #5a8cff;
  }
  html, body {
    margin: 0;
    width: 1200px;
    height: 1200px;
    overflow: hidden;
    background: var(--stage);
  }
  .board {
    position: relative;
    width: 1200px;
    height: 1200px;
  }
  .banner {
    position: absolute;
    left: 84px;
    width: 1027px;
    height: 510px;
    display: block;
  }
  .banner--violet { top: 71px; }
  .banner--teal { top: 618px; }
  .script-word {
    font-family: "Allura", cursive;
    fill: var(--white);
  }
  .hero-word {
    font-family: "Archivo Black", sans-serif;
    letter-spacing: -4px;
  }
  .brand-name {
    font-family: "Archivo Black", sans-serif;
    fill: var(--navy);
  }
  .brand-dot { fill: var(--navy); }
</style>
</head>
<body>
<main class="board">

  <svg class="banner banner--violet" viewBox="0 0 1027 510" xmlns="http://www.w3.org/2000/svg">
    <defs>
      <linearGradient id="violet-sky" x1="0" y1="0" x2="1" y2="1">
        <stop offset="0" stop-color="var(--violet-deep)"/>
        <stop offset="0.5" stop-color="var(--violet-mid)"/>
        <stop offset="1" stop-color="var(--violet-deep)"/>
      </linearGradient>
      <radialGradient id="violet-bloom" cx="0.5" cy="0.5" r="0.5">
        <stop offset="0" stop-color="var(--bloom-pink)" stop-opacity="0.85"/>
        <stop offset="1" stop-color="var(--bloom-pink)" stop-opacity="0"/>
      </radialGradient>
      <radialGradient id="violet-haze" cx="0.5" cy="0.5" r="0.5">
        <stop offset="0" stop-color="var(--violet-glow)" stop-opacity="0.8"/>
        <stop offset="1" stop-color="var(--violet-glow)" stop-opacity="0"/>
      </radialGradient>
      <linearGradient id="violet-word" x1="0" y1="0" x2="1" y2="0.4">
        <stop offset="0" stop-color="var(--word-light)"/>
        <stop offset="0.35" stop-color="var(--word-pink)"/>
        <stop offset="0.7" stop-color="var(--word-blue)"/>
        <stop offset="1" stop-color="var(--word-pink)"/>
      </linearGradient>
    </defs>
    <g class="photo" role="img" aria-label="Photo of pink peony flowers with a butterfly on a soft violet background">
      <rect width="1027" height="510" fill="url(#violet-sky)"/>
      <ellipse cx="560" cy="200" rx="260" ry="220" fill="url(#violet-bloom)"/>
      <ellipse cx="900" cy="280" rx="200" ry="180" fill="url(#violet-haze)"/>
      <ellipse cx="260" cy="130" rx="120" ry="110" fill="url(#violet-bloom)" opacity="0.6"/>
    </g>
    <text class="hero-word" x="244" y="321" font-size="168" fill="url(#violet-word)" opacity="0.92">Hope</text>
    <text class="script-word" x="280" y="232" font-size="120">Keep</text>
    <text class="script-word" x="500" y="370" font-size="120">Rising</text>
    <path class="sweep" d="M0 458 Q513 340 1027 467 L1027 510 L0 510 Z" fill="var(--white)"/>
    <g class="brand">
      <text class="brand-name" x="300" y="460" font-size="22" textLength="360" lengthAdjust="spacingAndGlyphs">From Harvest Crown TV Family</text>
      <circle class="brand-dot" cx="684" cy="452" r="18"/>
    </g>
  </svg>

  <svg class="banner banner--teal" viewBox="0 0 1027 510" xmlns="http://www.w3.org/2000/svg">
    <defs>
      <linearGradient id="teal-sky" x1="0" y1="0" x2="1" y2="1">
        <stop offset="0" stop-color="var(--teal-mid)"/>
        <stop offset="0.5" stop-color="var(--teal-deep)"/>
        <stop offset="1" stop-color="var(--teal-mid)"/>
      </linearGradient>
      <radialGradient id="teal-bloom" cx="0.5" cy="0.5" r="0.5">
        <stop offset="0" stop-color="var(--bloom-purple)" stop-opacity="0.85"/>
        <stop offset="1" stop-color="var(--bloom-purple)" stop-opacity="0"/>
      </radialGradient>
      <radialGradient id="teal-haze" cx="0.5" cy="0.5" r="0.5">
        <stop offset="0" stop-color="var(--teal-glow)" stop-opacity="0.7"/>
        <stop offset="1" stop-color="var(--teal-glow)" stop-opacity="0"/>
      </radialGradient>
      <linearGradient id="teal-word" x1="0" y1="0" x2="1" y2="0.4">
        <stop offset="0" stop-color="var(--teal-glow)"/>
        <stop offset="0.35" stop-color="var(--word-light)"/>
        <stop offset="0.7" stop-color="var(--word-blue)"/>
        <stop offset="1" stop-color="var(--word-light)"/>
      </linearGradient>
    </defs>
    <g class="photo" role="img" aria-label="Photo of purple peony flowers with a butterfly on a soft teal background">
      <rect width="1027" height="510" fill="url(#teal-sky)"/>
      <ellipse cx="560" cy="200" rx="260" ry="220" fill="url(#teal-bloom)"/>
      <ellipse cx="920" cy="260" rx="190" ry="170" fill="url(#teal-haze)"/>
      <ellipse cx="260" cy="130" rx="120" ry="110" fill="url(#teal-bloom)" opacity="0.6"/>
    </g>
    <text class="hero-word" x="244" y="321" font-size="168" fill="url(#teal-word)" opacity="0.92">Hope</text>
    <text class="script-word" x="280" y="232" font-size="120">Keep</text>
    <text class="script-word" x="500" y="370" font-size="120">Rising</text>
    <path class="sweep" d="M0 458 Q513 340 1027 467 L1027 510 L0 510 Z" fill="var(--white)"/>
    <g class="brand">
      <text class="brand-name" x="300" y="460" font-size="22" textLength="360" lengthAdjust="spacingAndGlyphs">From Harvest Crown TV Family</text>
      <circle class="brand-dot" cx="684" cy="452" r="18"/>
    </g>
  </svg>

</main>
</body>
</html>
```